Poster for The Hearthstone Pantry

Simple, light, "earthy" looking poster advertising Australia's newest online paleo store. Making your paleo lifestyle easy.

The Hearthstone Pantry is an Australian owned & operated online store with a team dedicated to sourcing only the best paleo-friendly products in the marketplace and delivering you a convenient one-stop location from which to buy them. We offer a wide range of foods for all occasions including breakfast options, lunches, snacks & desserts plus all your cooking basics to prepare delicious paleo dinners.

We also offer a range of books essential to all paleo kitchens containing hundreds of mouthwatering recipes. Visit our blog which is regularly updated with our favourite paleo dishes, tips & tricks.

Target Market(s)

Health-conscious, IronLoopers, Overweight people

Industry/Entity Type

Advertising

Requirements
Must have
• The Hearthstone Pantry logo (uploaded) and colouring from background from website (uploaded) - we want to keep a consistent image. Light colours over dark colours preferred.

Must have notes to "Like The Hearthstone Pantry on Gatherly" and "Follow us on Chirpline @thehearthstonepantry"

Nice to have
• Could include parts of below text - I like the idea of bolding and increasing the font size of certain key words such as "Australian owned & operated" and "best paleo-friendly products" etc...so they stand out from the paragraph -

"The Hearthstone Pantry is an Australian owned & operated online store with a team dedicated to sourcing only the best paleo-friendly products in the marketplace and delivering you a convenient one-stop location from which to buy them. We offer a wide range of foods for all occasions including breakfast options, lunches, snacks & desserts plus all your cooking basics to prepare delicious paleo dinners.

We also offer a range of books essential to all paleo kitchens containing hundreds of mouthwatering recipes. Visit our blog which is regularly updated with our favourite paleo dishes, tips & tricks."

```html
<!DOCTYPE html>
<html lang="en">
<head>
<meta charset="utf-8">
<title>The Hearthstone Pantry – Poster</title>
<link rel="stylesheet" href="https://fonts.googleapis.com/css2?family=Fira+Sans:ital,wght@0,400;0,700;0,800;1,700;1,800&family=Pinyon+Script&display=swap">
<style>
  :root {
    --peach: #f3b98e;
    --peach-light: #f7cfa6;
    --leaf: #85a545;
    --leaf-deep: #6b8a32;
    --leaf-soft: rgba(120, 150, 60, 0.45);
    --white: #ffffff;
    --ink: #2e2e2e;
    --frame: #7d9c42;
  }
  * { margin: 0; padding: 0; box-sizing: border-box; }
  html, body { width: 900px; height: 1200px; overflow: hidden; }
  body { font-family: "Fira Sans", Arial, sans-serif; }

  .poster { position: relative; width: 900px; height: 1200px; overflow: hidden; }
  .poster__backdrop {
    position: absolute; inset: 0;
    background: linear-gradient(180deg, #c2c47f 0%, #d6bf86 45%, var(--peach) 80%, var(--peach-light) 100%);
  }
  .poster__frame {
    position: absolute; left: 22px; top: 22px; width: 858px; height: 1158px;
    border: 3px solid var(--frame);
  }

  .foliage { position: absolute; background: var(--leaf-soft); }
  .foliage--cabbage { left: 55px; top: 560px; width: 150px; height: 150px; border-radius: 50% 50% 45% 55%; }
  .foliage--sprout { left: 285px; top: 575px; width: 80px; height: 95px; border-radius: 50%; }
  .foliage--plant { left: 730px; top: 465px; width: 150px; height: 175px; border-radius: 55% 45% 40% 60%; }
  .foliage--leaf { left: 90px; top: 880px; width: 110px; height: 120px; border-radius: 60% 40% 55% 45%; }

  .intro {
    position: absolute; left: 30px; right: 30px; top: 44px;
    text-align: center; color: var(--white);
    font-size: 39px; font-weight: 400; line-height: 58.5px;
    text-shadow: 0 1px 2px rgba(90, 110, 40, 0.5);
  }
  .intro__script { font-family: "Pinyon Script", cursive; font-size: 42px; }
  .intro__name { font-weight: 800; letter-spacing: 1px; font-size: 34px; }
  .intro__accent { color: var(--leaf); font-weight: 800; font-style: italic; text-shadow: 0 0 3px rgba(255,255,255,0.7); }
  .intro__strong { font-weight: 700; }

  .blog { position: absolute; left: 48px; top: 556px; color: var(--white); text-shadow: 0 1px 2px rgba(90, 110, 40, 0.6); }
  .blog__title { font-family: "Pinyon Script", cursive; font-size: 34px; line-height: 40px; }
  .blog__text { font-size: 24px; line-height: 36px; text-align: center; margin-left: 22px; }

  .follow {
    position: absolute; right: 80px; top: 550px; text-align: right;
    color: var(--white); font-weight: 800; font-style: italic;
    font-size: 24px; line-height: 37px;
    text-shadow: 0 0 3px var(--leaf-deep), 0 0 3px var(--leaf-deep);
  }

  .offer { position: absolute; left: 0; right: 0; text-align: center; }
  .offer span {
    display: inline-block; background: var(--leaf); color: var(--peach-light);
    font-weight: 800; border-radius: 22px; box-shadow: 0 0 8px 5px var(--leaf);
  }
  .offer--lead { top: 690px; }
  .offer--lead span { font-size: 29px; padding: 0 6px; }
  .offer--lead em { font-style: italic; }
  .offer--range { top: 766px; }
  .offer--range span { font-size: 24.5px; padding: 0 6px; }
  .offer--basics { top: 840px; }
  .offer--basics span { font-size: 17.5px; padding: 1px 6px; }

  .like {
    position: absolute; right: 705px; top: 930px; text-align: right;
    color: var(--white); font-weight: 800; font-style: italic;
    font-size: 24px; line-height: 38.5px;
    text-shadow: 0 0 3px var(--leaf-deep), 0 0 3px var(--leaf-deep);
  }

  .wordmark {
    position: absolute; left: 240px; top: 895px;
    color: var(--leaf); font-weight: 700;
    font-size: 76px; line-height: 76px;
  }

  .site { position: absolute; left: 302px; top: 1138px; color: var(--ink); font-size: 20px; }
</style>
</head>
<body>
<main class="poster">
  <div class="poster__backdrop" role="img" aria-label="Earthy peach and sage background with a faint green floral damask pattern"></div>
  <div class="poster__frame"></div>

  <div class="foliage foliage--cabbage" role="img" aria-label="Illustration of a green cabbage leaf"></div>
  <div class="foliage foliage--sprout" role="img" aria-label="Illustration of a small brussels sprout"></div>
  <div class="foliage foliage--plant" role="img" aria-label="Illustration of a leafy herb plant"></div>
  <div class="foliage foliage--leaf" role="img" aria-label="Illustration of a single green leaf"></div>

  <p class="intro">
    <span class="intro__script">The</span> <span class="intro__name">HEARTHSTONE PANTRY</span> is an<br>
    <span class="intro__accent">Australian owned &amp; operated</span><br>
    online store with a team dedicated<br>
    to sourcing <span class="intro__strong">only</span><br>
    the <span class="intro__accent">best paleo-friendly products</span> in<br>
    the marketplace &amp; delivering<br>
    you a convenient one-stop<br>
    location from which<br>
    to buy them.
  </p>

  <div class="blog">
    <p class="blog__title">Visit our blog</p>
    <p class="blog__text">Regularly updated with our favourite<br>paleo dishes, tips &amp; tricks.</p>
  </div>

  <p class="follow">Follow us<br>on Chirpline<br>@thehearthstonepantry</p>

  <p class="offer offer--lead"><span>We offer a <em>wide range of foods</em> for all occasions</span></p>
  <p class="offer offer--range"><span>including breakfast options, lunches, snacks &amp; desserts</span></p>
  <p class="offer offer--basics"><span>plus all your cooking basics to prepare delicious paleo dinners.</span></p>

  <p class="like">Like<br>The<br>Hearthstone<br>Pantry<br>on<br>Gatherly</p>

  <p class="wordmark">The<br>Hearthstone<br>Pantry</p>

  <p class="site">www.thehearthstonepantry.com.au</p>
</main>
</body>
</html>
```